Vintage themed home decor Shopify store needs sales promotion banner ads

"The Quiet Lantern Works" is an Australian based lifestyle home decor store that sells vintage, retro and antique relic replicas and reproduction items online to their local customers Australia wide.

We need banner ads for our store home page slider that promotes our unique products, new stock arrival and calls store visitors to to buy from our different product collections.

We anticipate that we will need multiple banner ads, primarily for the following product collections:
1. Sundials & Compass
2. Airplane models
3. Magnifying glass
4. Clocks & Watches

Banners could also be generic with generic discount coupon promotions.

Banners should be based around the theme of our store and products which gives a sense of colonial / vintage lifestyle and that they compliment the colour & theme of the store.

Banner Size: 1600 x 800 px

Please find attached some samples of the types of banner ads we have in mind and also our logo. Product images can be supplied if they are required to be used in the ads.

Website URL: https://quietlanternworks.example

Target Market(s)

mostly Males aged between 35-65.
Products ideally for man-cave & office decor.

Industry/Entity Type

Home And Garden

Font styles to use
Serif
Decorative
Script

Requirements
Must have
• some product images
Nice to have
• lifestyle shots.
• blank space to insert for a coupon code
Should not have
• caricatures & cartoon

```html
<!DOCTYPE html>
<html lang="en">
<head>
<meta charset="utf-8">
<title>The Quiet Lantern Works – Collection Banners</title>
<link href="https://fonts.googleapis.com/css2?family=Arvo:wght@400;700&family=Lato:wght@400;700&display=swap" rel="stylesheet">
<style>
  :root {
    --page: #ffffff;
    --banner-bg: #eeeeee;
    --banner-line: #d6d6d6;
    --ink: #1f1f1f;
    --orange: #f26a22;
    --button: #262626;
    --white: #ffffff;
    --brass: #8a6a3e;
    --wood: #6b3f22;
    --plane: #c9a53a;
    --clock: #d9d4c8;
    --mark: #777777;
  }
  * { box-sizing: border-box; margin: 0; padding: 0; }
  html, body { width: 859px; height: 1200px; overflow: hidden; background: var(--page); }
  .sheet { position: relative; width: 859px; height: 1200px; }

  .banner {
    position: absolute; left: 167px; width: 521px; height: 256px;
    background: var(--banner-bg);
    box-shadow: 0 6px 14px rgba(0,0,0,0.18);
    overflow: hidden;
  }
  .banner::before, .banner::after {
    content: ""; position: absolute; left: 0; right: 0; height: 1px; background: var(--banner-line); z-index: 3;
  }
  .banner::before { top: 5px; }
  .banner::after { bottom: 5px; }
  .banner--magnifier { top: 24px; }
  .banner--aeroplane { top: 308px; }
  .banner--clocks { top: 591px; }
  .banner--sundials { top: 871px; }

  .banner__title {
    position: absolute; z-index: 2; font-family: "Arvo", serif; font-weight: 400;
    font-size: 18px; letter-spacing: 3.4px; color: var(--ink); text-transform: uppercase; white-space: nowrap;
  }
  .banner--text-left .banner__title { left: 10px; top: 86px; }
  .banner--text-right .banner__title { right: 10px; top: 76px; }

  .ribbon {
    position: absolute; z-index: 2; top: 122px; height: 45px;
    background: var(--orange); color: var(--white); text-align: center;
    display: flex; flex-direction: column; justify-content: center;
  }
  .banner--text-left .ribbon { left: 0; width: 296px; padding-right: 30px; clip-path: polygon(0 0, 100% 0, 97% 50%, 91% 100%, 0 100%); }
  .banner--text-right .ribbon { right: 0; width: 292px; padding-left: 28px; clip-path: polygon(0 0, 100% 0, 100% 100%, 9% 100%, 3% 50%); }
  .ribbon__lead { font-family: "Lato", sans-serif; font-size: 7.5px; letter-spacing: 0.6px; text-transform: uppercase; line-height: 1.1; }
  .ribbon__code { font-family: "Arvo", serif; font-weight: 700; font-size: 15px; letter-spacing: 1.5px; line-height: 1.2; }

  .shop-button {
    position: absolute; z-index: 2; top: 185px; width: 171px; height: 36px;
    background: var(--button); color: var(--white); text-decoration: none;
    font-family: "Lato", sans-serif; font-size: 15px; letter-spacing: 2.6px;
    display: flex; align-items: center; justify-content: center; text-transform: uppercase;
  }
  .shop-button::after { content: ""; position: absolute; inset: 3px 0; border-top: 1px solid rgba(255,255,255,0.7); border-bottom: 1px solid rgba(255,255,255,0.7); }
  .banner--text-left .shop-button { left: 37px; }
  .banner--text-right .shop-button { left: 299px; }

  .product { position: absolute; z-index: 1; }
  .product--magnifier { left: 298px; top: 24px; width: 191px; height: 205px; border-radius: 40% 40% 18px 18px; background: linear-gradient(160deg, #c9c2b2, var(--brass) 55%, var(--wood)); }
  .product--aeroplane { left: 0; top: 92px; width: 225px; height: 95px; border-radius: 40px; background: linear-gradient(90deg, var(--plane), #a7883a 60%, var(--plane)); }
  .product--clock { left: 334px; top: 42px; width: 161px; height: 179px; border-radius: 50%; background: radial-gradient(circle, #8a6d48 18%, var(--clock) 22%, #f2efe8 70%, #a77b4d 74%); }
  .product--sundial { left: 30px; top: 42px; width: 190px; height: 186px; border-radius: 18px; background: linear-gradient(160deg, #4d4a45, var(--brass) 50%, var(--wood)); }

  .brand-mark {
    position: absolute; z-index: 3; bottom: 11px; font-family: "Lato", sans-serif; font-size: 6.5px; color: var(--mark); letter-spacing: 0.3px; white-space: nowrap;
  }
  .banner--text-left .brand-mark { right: 8px; }
  .banner--text-right .brand-mark { left: 8px; }
</style>
</head>
<body>
<main class="sheet">

  <section class="banner banner--magnifier banner--text-left">
    <h2 class="banner__title">Magnifying Glass</h2>
    <div class="ribbon"><span class="ribbon__lead">Get 5% off! Use coupon code</span><span class="ribbon__code">AIYPWZQP</span></div>
    <a class="shop-button" href="https://quietlanternworks.example">Shop Now</a>
    <div class="product product--magnifier" role="img" aria-label="Brass desk magnifying glass on a wooden base"></div>
    <span class="brand-mark">The Quiet Lantern Works</span>
  </section>

  <section class="banner banner--aeroplane banner--text-right">
    <div class="product product--aeroplane" role="img" aria-label="Yellow vintage biplane model"></div>
    <h2 class="banner__title">Aeroplane Models</h2>
    <div class="ribbon"><span class="ribbon__lead">Get 5% off! Use coupon code</span><span class="ribbon__code">AIYPWZQP</span></div>
    <a class="shop-button" href="https://quietlanternworks.example">Shop Now</a>
    <span class="brand-mark">The Quiet Lantern Works</span>
  </section>

  <section class="banner banner--clocks banner--text-left">
    <h2 class="banner__title">Clocks &amp; Watches</h2>
    <div class="ribbon"><span class="ribbon__lead">Get 5% off! Use coupon code</span><span class="ribbon__code">AIYPWZQP</span></div>
    <a class="shop-button" href="https://quietlanternworks.example">Shop Now</a>
    <div class="product product--clock" role="img" aria-label="Vintage wall clock with exposed gears and a copper rim"></div>
    <span class="brand-mark">The Quiet Lantern Works</span>
  </section>

  <section class="banner banner--sundials banner--text-right">
    <div class="product product--sundial" role="img" aria-label="Brass sundial compass in a wooden box beside a gimballed compass on a stand"></div>
    <h2 class="banner__title">Sundials &amp; Compass</h2>
    <div class="ribbon"><span class="ribbon__lead">Get 5% off! Use coupon code</span><span class="ribbon__code">AIYPWZQP</span></div>
    <a class="shop-button" href="https://quietlanternworks.example">Shop Now</a>
    <span class="brand-mark">The Quiet Lantern Works</span>
  </section>

</main>
</body>
</html>
```